Design a New Business Card for Our Company

We are looking for fresh, unique, and a modern business card that reflects our roots as digital marketing agency focused on SEM.

Industry/Entity Type

Marketing

Contact Information for Business Card

looking for very unique out of the box designs. clean and modern that compliments our logo

Requirements
Must have
• colors should match our logo
• Front should have name, address, email, and phone/fax of the person, phone/fax are the same number
• back should have our url

```html
<!DOCTYPE html>
<html lang="en">
<head>
<meta charset="utf-8">
<title>Brightwell Business Card</title>
<link rel="stylesheet" href="https://fonts.googleapis.com/css2?family=Questrial&family=Great+Vibes&family=Alegreya:ital,wght@1,400&display=swap">
<style>
  :root {
    --paper: #f3f4f4;
    --brand-grey: #5f7572;
    --brand-blue: #1f63e0;
    --text-grey: #5a6466;
    --accent-light: #5fc4ea;
    --accent-deep: #2f56d8;
  }
  html, body {
    margin: 0;
    padding: 0;
    width: 1200px;
    height: 720px;
    overflow: hidden;
    background: var(--paper);
  }
  .card {
    position: relative;
    width: 1200px;
    height: 720px;
    background: var(--paper);
    overflow: hidden;
  }
  .brand-dot {
    position: absolute;
    left: 72px;
    top: 78px;
    width: 128px;
    height: 128px;
    border-radius: 50%;
    background: var(--brand-blue);
  }
  .brand-name {
    position: absolute;
    left: 232px;
    top: 56px;
    margin: 0;
    font-family: "Questrial", sans-serif;
    font-weight: 400;
    font-size: 136px;
    line-height: 1;
    letter-spacing: -2px;
    color: var(--brand-grey);
  }
  .person {
    position: absolute;
    right: 62px;
    top: 252px;
    text-align: right;
  }
  .person-name {
    margin: 0;
    font-family: "Great Vibes", cursive;
    font-weight: 400;
    font-size: 74px;
    line-height: 1;
    color: var(--brand-blue);
  }
  .person-title {
    margin: -4px 0 0;
    font-family: "Great Vibes", cursive;
    font-size: 52px;
    line-height: 1;
    color: var(--text-grey);
  }
  .contact {
    position: absolute;
    margin: 0;
    font-family: "Alegreya", serif;
    font-style: italic;
    font-weight: 400;
    font-size: 36px;
    line-height: 48px;
    color: var(--text-grey);
  }
  .contact-address { left: 144px; top: 380px; }
  .contact-phone { left: 416px; top: 556px; }
  .accent-block {
    position: absolute;
    left: 60px;
    top: 540px;
    width: 118px;
    height: 118px;
    background: linear-gradient(135deg, var(--accent-light), var(--accent-deep));
  }
</style>
</head>
<body>
  <div class="card">
    <span class="brand-dot"></span>
    <h1 class="brand-name">brightwell</h1>

    <div class="person">
      <p class="person-name">Mr. Alden Brightwell</p>
      <p class="person-title">Job Title</p>
    </div>

    <p class="contact contact-address">
      1234 Main Street<br>
      Anytown, State ZIP<br>
      no_reply@example.com
    </p>

    <p class="contact contact-phone">
      Tel. No.: 123-456-7890<br>
      Fax No.: 123-456-7890
    </p>

    <div class="accent-block" role="img" aria-label="Decorative accent of overlapping coloured squares"></div>
  </div>
</body>
</html>
```